New business card, letter head, email signature and Portfolio for our Security company.

We are an Elite security company that provides a top quality manpower services to protect high rise buildings, retail and all type of properties and would like a new business card/logo look.

- We would like the spot UV design.
- Matt black (double sided).
- We would like to incorporate a royal blue colour (feel free to experiment with it).
- Feel free to try different lengths with the card to make it stand out more than a normal business card.
- We would like the logo to be an eagle eye in the background (shines when card is tilted slightly in the background, either on the front, back or both sides of the card). Image attached as an example of eye shape (colour to be either black or royal blue).
- MAVRIN OAK GUARD PATROLS PTY. LTD. and MOGP to be placed on one side of the card and on the other side of the card to have;

- Name in slightly bigger font than the position (directly on the bottom on the name).
- Mobile number
- Email address
- Website email address
- PO BOX address

Can we please have the files in a format that we can edit.

Reason: I need to consult my business partner with the designs so far and will make a decision from there.

Target Market(s)

Security Industry

Industry/Entity Type

Business

Contact Information for Business Card

- Mobile number
- Email address
- Website email address
- PO BOX address

Logo Text

MOGP and underneath the MOGP please add MAVRIN OAK GUARD PATROLS PTY. LTD.

Font styles to use
Other font styles liked:
• bold type font

Colors
0255a3
000000

Requirements
Must have
• We are an Elite security company that provides a top quality manpower services to protect high rise buildings, retail and all type of properties and would like a new business card/logo look.
• - We would like the spot UV design.
• - Matt black (double sided).
• - We would like to incorporate a royal blue colour (feel free to experiment with it).
• - Feel free to try different lengths with the card to make it stand out more than a normal business card.
• - We would like the logo to be an eagle eye in the background (shines when card is tilted slightly in the background, either on the front, back or both sides of the card). Image attached as an example of eye shape (colour to be either black or royal blue).
• - MAVRIN OAK GUARD PATROLS PTY. LTD. and MOGP to be placed on one side of the card and on the other side of the card to have;
• - Name in slightly bigger font than the position (directly on the bottom on the name).
• - Mobile number
• - Email address
• - Website email address
• - PO BOX address
• Can we please have the files in a format that we can edit.
Nice to have
• Feel free to try different lengths with the card to make it stand out more than a normal business card.
• Please find "URBAN JUNGLE" font attached and incorporate MOGP into the same style with building's inside the MOGP bold front also add MAVRIN into the bottom part of the S and follow on E - Elite on the bottom S - SECURITY on the bottom S - SERVICES on the bottom of each letter.
• other than that, I'll be happy with a bold modern font for the MOGP and MAVRIN OAK GUARD PATROLS in a bold and thinner font underneath.

```html
<!DOCTYPE html>
<html lang="en">
<head>
<meta charset="utf-8">
<title>MOGP Business Card</title>
<link href="https://fonts.googleapis.com/css2?family=Open+Sans:wght@400;600;700;800&display=swap" rel="stylesheet">
<style>
  :root {
    --stage: #3a3330;
    --card-black: #111111;
    --royal-blue: #0255a3;
    --white: #ffffff;
    --uv-grey: #3c3c3c;
    --divider: #4a4a4a;
  }
  * { box-sizing: border-box; margin: 0; padding: 0; }
  html, body {
    width: 1200px;
    height: 780px;
    overflow: hidden;
    background: var(--stage);
    font-family: "Open Sans", Arial, sans-serif;
  }
  .stage {
    position: relative;
    width: 1200px;
    height: 780px;
  }
  .card {
    position: absolute;
    top: 235px;
    width: 540px;
    height: 310px;
    background: var(--card-black);
    overflow: hidden;
    box-shadow: 0 10px 28px rgba(0,0,0,0.45);
  }
  .card--back { left: 40px; }
  .card--front { left: 620px; }

  .card__band {
    position: absolute;
    left: 0; right: 0; bottom: 0;
    height: 48px;
    background: var(--royal-blue);
    border-top: 4px solid var(--white);
    display: flex;
    align-items: center;
    justify-content: center;
    color: var(--white);
    font-size: 15px;
    font-weight: 600;
    letter-spacing: 0.5px;
  }
  .card--back .card__band {
    letter-spacing: 3px;
    font-size: 14px;
    font-weight: 400;
  }

  .wordmark {
    font-weight: 800;
    line-height: 1;
  }
  .wordmark__initials {
    display: block;
    font-size: 72px;
    letter-spacing: 8px;
  }
  .wordmark__name {
    display: block;
    font-size: 13px;
    letter-spacing: 1.5px;
    margin-top: 6px;
  }

  .card--back .wordmark {
    position: absolute;
    left: 0; right: 0;
    top: 76px;
    text-align: center;
    color: var(--uv-grey);
  }

  .card--front .wordmark {
    position: absolute;
    left: 36px;
    top: 86px;
    width: 230px;
    text-align: center;
    color: var(--white);
  }
  .card__divider {
    position: absolute;
    left: 286px;
    top: 60px;
    width: 1px;
    height: 150px;
    background: var(--divider);
  }
  .contact {
    position: absolute;
    left: 306px;
    top: 66px;
    color: var(--white);
  }
  .contact__name {
    font-size: 22px;
    font-weight: 700;
    line-height: 1.1;
  }
  .contact__role {
    font-size: 14px;
    font-weight: 600;
    color: var(--royal-blue);
    margin-bottom: 18px;
  }
  .contact__list { list-style: none; }
  .contact__item {
    display: flex;
    align-items: center;
    gap: 9px;
    font-size: 13.5px;
    font-weight: 600;
    margin-bottom: 7px;
  }
  .contact__icon {
    width: 18px;
    height: 18px;
    flex: none;
  }
</style>
</head>
<body>
<main class="stage">

  <section class="card card--back" aria-label="Business card back">
    <div class="wordmark">
      <span class="wordmark__initials">MOGP</span>
      <span class="wordmark__name">MAVRIN OAK GUARD PATROLS</span>
    </div>
    <div class="card__band">WWW.MOGPPATROLS.CO.NZ</div>
  </section>

  <section class="card card--front" aria-label="Business card front">
    <div class="wordmark">
      <span class="wordmark__initials">MOGP</span>
      <span class="wordmark__name">MAVRIN OAK GUARD PATROLS</span>
    </div>
    <div class="card__divider"></div>
    <div class="contact">
      <p class="contact__name">Employee Name</p>
      <p class="contact__role">Manager</p>
      <ul class="contact__list">
        <li class="contact__item">
          <svg class="contact__icon" viewBox="0 0 18 18" aria-hidden="true">
            <rect width="18" height="18" fill="#0255a3"/>
            <rect x="6" y="3" width="6" height="12" rx="1" fill="none" stroke="#fff" stroke-width="1.4"/>
            <circle cx="9" cy="12.8" r="0.8" fill="#fff"/>
          </svg>
          0210 555 014
        </li>
        <li class="contact__item">
          <svg class="contact__icon" viewBox="0 0 18 18" aria-hidden="true">
            <rect width="18" height="18" fill="#0255a3"/>
            <rect x="3" y="5" width="12" height="8" fill="none" stroke="#fff" stroke-width="1.3"/>
            <path d="M3 5 L9 10 L15 5" fill="none" stroke="#fff" stroke-width="1.3"/>
          </svg>
          contact@mogpmail.net.nz
        </li>
        <li class="contact__item">
          <svg class="contact__icon" viewBox="0 0 18 18" aria-hidden="true">
            <rect width="18" height="18" fill="#0255a3"/>
            <circle cx="9" cy="9" r="5.5" fill="none" stroke="#fff" stroke-width="1.2"/>
            <ellipse cx="9" cy="9" rx="2.4" ry="5.5" fill="none" stroke="#fff" stroke-width="1"/>
            <line x1="3.5" y1="9" x2="14.5" y2="9" stroke="#fff" stroke-width="1"/>
          </svg>
          www.mogppatrols.co.nz
        </li>
      </ul>
    </div>
    <div class="card__band">P.O. Box 482, Harbour Lane, Kelvin Grove, New Zealand</div>
  </section>

</main>
</body>
</html>
```